Surviving Domestic Violence Flyer

I need a flyer that "POPS" to attract participants for my research project. I have added the important information on my draft flyer.

```html
<!DOCTYPE html>
<html lang="en">
<head>
<meta charset="utf-8">
<title>Survivor Resources Study – Request for Study Participants</title>
<link rel="stylesheet" href="https://fonts.googleapis.com/css2?family=Anton&family=Arimo:wght@400;700&display=swap">
<style>
  :root {
    --ink: #000000;
    --paper: #ffffff;
    --alert-red: #e3000f;
    --deep-red: #c4000c;
    --smoke: #3a3a3a;
  }
  * { box-sizing: border-box; margin: 0; padding: 0; }
  html, body { width: 1200px; height: 848px; overflow: hidden; background: var(--ink); }
  .flyer {
    position: relative; width: 1200px; height: 848px; overflow: hidden;
    background: var(--ink); font-family: "Arimo", Arial, sans-serif; color: var(--paper);
  }
  .portrait-area {
    position: absolute; left: 420px; top: 140px; width: 580px; height: 708px;
    background:
      radial-gradient(ellipse 45% 55% at 55% 55%, #5a5a5a 0%, #2a2a2a 45%, rgba(0,0,0,0) 80%),
      radial-gradient(ellipse 60% 40% at 50% 15%, #4a4a4a 0%, rgba(0,0,0,0) 70%),
      var(--ink);
  }
  .headline {
    position: absolute; left: 40px; top: 4px; width: 950px;
    font-family: "Anton", "Arial Narrow", sans-serif; font-size: 70px; line-height: 86px;
    color: var(--paper); letter-spacing: 0.5px;
    -webkit-text-stroke: 8px var(--alert-red); paint-order: stroke fill;
  }
  .study-title {
    position: absolute; left: 35px; top: 97px; width: 960px; height: 31px;
    background: var(--paper); color: var(--deep-red);
    font-size: 19px; font-variant: small-caps; letter-spacing: 3.4px;
    display: flex; align-items: center; justify-content: center; white-space: nowrap;
  }
  .criteria { position: absolute; left: 14px; top: 150px; width: 430px; list-style: none; }
  .criteria li, .contact {
    position: relative; color: var(--alert-red); font-size: 20px; line-height: 23px;
    -webkit-text-stroke: 3px var(--paper); paint-order: stroke fill;
  }
  .bullet {
    position: absolute; left: 0; width: 16px; height: 16px;
    background: var(--alert-red); border: 2px solid var(--paper);
  }
  .criteria .text { display: block; padding-left: 26px; }
  .q1 { margin-bottom: 28px; } .q1 .bullet { top: 6px; }
  .q2 { margin-bottom: 12px; } .q2 .bullet { top: 4px; }
  .q3 { padding-top: 26px; margin-bottom: 12px; } .q3 .bullet { top: 0; }
  .q4 { padding-top: 26px; margin-bottom: 12px; } .q4 .bullet { top: 0; }
  .q5 { padding-top: 26px; } .q5 .bullet { top: 0; }
  .eligibility {
    position: absolute; left: 12px; top: 547px; width: 426px; height: 114px;
    background: var(--paper); border-radius: 10px; padding: 8px 10px 0 26px;
    color: var(--alert-red); font-size: 15px; line-height: 18.5px;
  }
  .eligibility p { position: relative; }
  .eligibility .bullet {
    left: -19px; top: 2px; width: 13px; height: 13px;
    background: var(--deep-red); border: 2px solid var(--smoke);
  }
  .eligibility p + p { margin-top: 6px; }
  .contact { position: absolute; left: 10px; top: 676px; width: 440px; font-size: 17px; line-height: 19px; }
  .contact .bullet { top: 2px; }
  .contact .text { display: block; padding-left: 24px; }
  .contact .email { padding-left: 0; }
  .credits { position: absolute; left: 36px; top: 764px; font-size: 14px; line-height: 18.5px; color: var(--paper); }
  .slip-prompt {
    position: absolute; left: 952px; top: 480px; width: 660px; text-align: center;
    transform: translate(-50%, -50%) rotate(-90deg);
    font-size: 50px; line-height: 56px; color: var(--paper);
    -webkit-text-stroke: 6px var(--alert-red); paint-order: stroke fill; white-space: nowrap;
  }
  .tear-slips { position: absolute; left: 998px; top: 4px; width: 202px; list-style: none; }
  .tear-slips li {
    height: 58px; margin-bottom: 3.8px; background: var(--paper); color: var(--ink);
    padding: 6px 0 0 12px;
  }
  .tear-slips .slip-name { display: block; font-size: 14px; line-height: 16px; }
  .tear-slips .slip-phone { display: block; font-size: 21px; line-height: 28px; }
  .restock-note {
    position: absolute; left: 1012px; top: 811px; font-size: 11px; line-height: 15px; color: var(--paper);
  }
</style>
</head>
<body>
<main class="flyer">
  <div class="portrait-area" role="img" aria-label="Dramatic dark close-up photograph of a woman's face looking at the viewer"></div>

  <h1 class="headline">Request for Study Participants</h1>
  <p class="study-title">Efficiency of Resources Available to Survivors of Domestic Violence</p>

  <ul class="criteria">
    <li class="q1"><span class="bullet"></span><span class="text">Are you a woman who is 18 years of age or older?</span></li>
    <li class="q2"><span class="bullet"></span><span class="text">Have you been the victim of domestic violence?</span></li>
    <li class="q3"><span class="bullet"></span><span class="text">Have you sought assistance with abuse in the last 12 months?</span></li>
    <li class="q4"><span class="bullet"></span><span class="text">Are you still in contact with the person that abused you?</span></li>
    <li class="q5"><span class="bullet"></span><span class="text">Are you willing and open to discuss your experience with abuse and your attempts to access services or resources?</span></li>
  </ul>

  <div class="eligibility">
    <p><span class="bullet"></span>If you answered Yes to all of the questions, you may be eligible to participate in a study to better under-stand the resources needed and services expected for survivors of domestic violence.</p>
    <p><span class="bullet"></span>Participants will be compensated for their time.</p>
  </div>

  <p class="contact"><span class="bullet"></span><span class="text">Please contact Dana Whitfield at 1(555)214-0386<br>or via</span><span class="text">e-mail&nbsp; survivorvoicesstudy@example.org</span></p>

  <div class="credits">
    <p>Principal investigator: Dana Whitfield</p>
    <p>Institutional affiliation: Lakeshore State University, Dept. of Criminology, Law, and Justice.</p>
    <p>Contact address: Post Office Box 310542, Brookhaven, IL, 60612</p>
  </div>

  <p class="slip-prompt">Please take information slip</p>

  <ul class="tear-slips">
    <li><span class="slip-name">Survivor Resources Study</span><span class="slip-phone">1(555) 214-0386</span></li>
    <li><span class="slip-name">Survivor Resources Study</span><span class="slip-phone">1(555) 214-0386</span></li>
    <li><span class="slip-name">Survivor Resources Study</span><span class="slip-phone">1(555) 214-0386</span></li>
    <li><span class="slip-name">Survivor Resources Study</span><span class="slip-phone">1(555) 214-0386</span></li>
    <li><span class="slip-name">Survivor Resources Study</span><span class="slip-phone">1(555) 214-0386</span></li>
    <li><span class="slip-name">Survivor Resources Study</span><span class="slip-phone">1(555) 214-0386</span></li>
    <li><span class="slip-name">Survivor Resources Study</span><span class="slip-phone">1(555) 214-0386</span></li>
    <li><span class="slip-name">Survivor Resources Study</span><span class="slip-phone">1(555) 214-0386</span></li>
    <li><span class="slip-name">Survivor Resources Study</span><span class="slip-phone">1(555) 214-0386</span></li>
    <li><span class="slip-name">Survivor Resources Study</span><span class="slip-phone">1(555) 214-0386</span></li>
    <li><span class="slip-name">Survivor Resources Study</span><span class="slip-phone">1(555) 214-0386</span></li>
    <li><span class="slip-name">Survivor Resources Study</span><span class="slip-phone">1(555) 214-0386</span></li>
    <li><span class="slip-name">Survivor Resources Study</span><span class="slip-phone">1(555) 214-0386</span></li>
  </ul>
  <p class="restock-note">Please inform Dana that info<br>slips ran out: 1(555) 214 - 0386</p>
</main>
</body>
</html>
```